Business Card for Toffee Parlour

I have a logo for my candy buffet business, and need a business card designed using that logo. Toffee Parlour designs and builds beautiful and delicious candy and dessert tables for all kinds of events. The card should be simple, modern, graphic, colorful, and use the Toffee Parlour Logo.

Target Market(s)

The target market is people hosting major parties and events. This includes brides getting married, parents hosting birthday parties/Sweet Sixteen/Bar Mitzvah/quinceanera parties, and companies hosting corporate events.

Industry/Entity Type

Business

Requirements
Must have
• The business card must have the logo, with or without the tag line.

The following information must be on the card:

Renata Hollis
CEO & Candy Stylist
415.372.6091
renata@toffeeparlourco.example
Nice to have
• I like the idea of having multiple colors of the same design so that several people receiving cards will each receive a different color. Perhaps 3-5 colors or variations on a basic card design.

```html
<!DOCTYPE html>
<html lang="en">
<head>
<meta charset="utf-8">
<title>Toffee Parlour – Business Card</title>
<link href="https://fonts.googleapis.com/css2?family=Lato:wght@400;700&display=swap" rel="stylesheet">
<style>
  :root {
    --backdrop: #e6e3df;
    --card: #ffffff;
    --ink: #231f20;
    --band-orange: #e98a30;
    --band-blue: #1676ab;
    --accent-dot: #e98a30;
    --stripe-1: #e98a30;
    --stripe-2: #1676ab;
    --stripe-3: #2a8a56;
    --stripe-4: #b8326f;
    --stripe-5: #2b2b2b;
    --icon-blue: #1676ab;
    --white: #ffffff;
  }
  * { margin: 0; padding: 0; box-sizing: border-box; }
  html, body { width: 1200px; height: 1000px; overflow: hidden; }
  body { background: var(--backdrop); position: relative; font-family: "Lato", sans-serif; color: var(--ink); }

  .card {
    position: absolute;
    width: 600px; height: 350px;
    background: var(--card);
    box-shadow: 4px 6px 14px rgba(0,0,0,0.25);
    overflow: hidden;
  }
  .card--front { left: 191px; top: 116px; }
  .card--back { left: 380px; top: 500px; }

  .stripes { position: absolute; left: 0; bottom: 0; width: 600px; height: 33px; display: block; }

  .wordmark {
    position: absolute;
    display: flex; align-items: center; justify-content: center;
    font-family: "Lato", sans-serif; font-weight: 400; color: var(--ink);
    white-space: nowrap; line-height: 1;
  }
  .wordmark__dot { flex: none; border-radius: 50%; background: var(--accent-dot); }

  .card--front .wordmark { left: 300px; top: 62px; width: 240px; height: 40px; gap: 10px; font-size: 30px; }
  .card--front .wordmark__dot { width: 18px; height: 18px; }

  .card--back .wordmark { left: 80px; top: 150px; width: 440px; height: 60px; gap: 16px; font-size: 46px; }
  .card--back .wordmark__dot { width: 28px; height: 28px; }

  .title-bands { position: absolute; left: 0; top: 106px; width: 600px; height: 66px; display: block; }
  .holder-name {
    position: absolute; left: 41px; top: 130px;
    font-weight: 700; font-size: 20px; color: var(--white); letter-spacing: 0.3px;
  }
  .holder-role {
    position: absolute; left: 280px; top: 128px;
    font-weight: 700; font-size: 20px; color: var(--white);
  }

  .contact { position: absolute; left: 280px; top: 194px; list-style: none; }
  .contact li { display: flex; align-items: center; height: 28px; font-size: 16.5px; }
  .contact svg { width: 14px; height: 14px; margin-right: 18px; flex: none; }
</style>
</head>
<body>

  <section class="card card--front" aria-label="Business card front">
    <div class="wordmark"><span class="wordmark__dot" aria-hidden="true"></span>Toffee Parlour</div>

    <svg class="title-bands" viewBox="0 0 600 66" aria-hidden="true">
      <polygon points="0,0 262,0 235,66 0,66" fill="var(--band-orange)"/>
      <polygon points="262,13 600,13 600,61 241,61" fill="var(--band-blue)"/>
    </svg>
    <p class="holder-name">RENATA HOLLIS</p>
    <p class="holder-role">CEO &amp; Candy Stylist</p>

    <ul class="contact">
      <li>
        <svg viewBox="0 0 24 24" aria-hidden="true"><path fill="var(--icon-blue)" d="M6.6 10.8a15.1 15.1 0 0 0 6.6 6.6l2.2-2.2c.3-.3.7-.4 1-.2 1.1.4 2.3.6 3.6.6.6 0 1 .4 1 1V20c0 .6-.4 1-1 1C10.6 21 3 13.4 3 4c0-.6.4-1 1-1h3.5c.6 0 1 .4 1 1 0 1.3.2 2.5.6 3.6.1.3 0 .7-.2 1z"/></svg>
        415.372.6091
      </li>
      <li>
        <svg viewBox="0 0 24 24" aria-hidden="true"><rect x="2" y="5" width="20" height="14" fill="none" stroke="var(--icon-blue)" stroke-width="2.2"/><polyline points="2,5 12,13 22,5" fill="none" stroke="var(--icon-blue)" stroke-width="2.2"/></svg>
        renata@toffeeparlourco.example
      </li>
      <li>
        <svg viewBox="0 0 24 24" aria-hidden="true"><g fill="none" stroke="var(--icon-blue)" stroke-width="1.8"><circle cx="12" cy="12" r="9.5"/><ellipse cx="12" cy="12" rx="4.2" ry="9.5"/><line x1="2.5" y1="12" x2="21.5" y2="12"/></g></svg>
        www.toffeeparlourco.example
      </li>
    </ul>

    <svg class="stripes" viewBox="0 0 600 33" aria-hidden="true">
      <polygon points="0,0 130,0 118,33 0,33" fill="var(--stripe-1)"/>
      <polygon points="130,0 262,0 250,33 118,33" fill="var(--stripe-2)"/>
      <polygon points="262,0 394,0 382,33 250,33" fill="var(--stripe-3)"/>
      <polygon points="394,0 526,0 514,33 382,33" fill="var(--stripe-4)"/>
      <polygon points="526,0 600,0 600,33 514,33" fill="var(--stripe-5)"/>
    </svg>
  </section>

  <section class="card card--back" aria-label="Business card back">
    <div class="wordmark"><span class="wordmark__dot" aria-hidden="true"></span>Toffee Parlour</div>

    <svg class="stripes" viewBox="0 0 600 33" aria-hidden="true">
      <polygon points="0,0 130,0 118,33 0,33" fill="var(--stripe-1)"/>
      <polygon points="130,0 262,0 250,33 118,33" fill="var(--stripe-2)"/>
      <polygon points="262,0 394,0 382,33 250,33" fill="var(--stripe-3)"/>
      <polygon points="394,0 526,0 514,33 382,33" fill="var(--stripe-4)"/>
      <polygon points="526,0 600,0 600,33 514,33" fill="var(--stripe-5)"/>
    </svg>
  </section>

</body>
</html>
```